website for local kavenda practicioner and yoga teacher trainer

The website should function primarily as:
A place where people can discover Kavenda and book sessions.
A central hub connecting all of my work.
A professional home that reflects my personality and approach.
Website design for Liesbet Oonwerk — Kavenda® Structural Integration practitioner, movement educator, yoga teacher and teacher trainer.
A website that can grow with future projects.
The website should feel: Warm, Human, Invitational, Professional, Accessible, Intelligent, Calm, Clear, Playful, Exploratory, Trustworthy
Avoid: New age aesthetics, Mystical clichés, Excessive spirituality, ”Guru" vibes, Overly clinical design, Corporate wellness branding, Busy layouts
Think: modern, grounded, curious and real.
My work combines three interconnected areas:
1.Bodywork: Touch, structure, awareness and one-on-one support.
2. Movement: Yoga, Pilates and embodied movement.
3. Education: Teacher trainings, workshops and continued learning.
Underlying values:
Curiosity over certainty
Possibility over perfection
Complexity without overwhelm
Science and lived experience together
Exploration rather than dogma
Human beings before methods
The primary goal of the website is to introduce people to Kavenda® Structural Integration and make it easy for them to:
Understand what Kavenda is
Discover whether it might be relevant for them
Learn what to expect from a session
Book an appointment
Booking should always feel visible and easy.
Secondary Goal: Present all other aspects of my work in one coherent place:
Yoga classes
Pilates classes
Teacher trainings
Workshops
Retreats
One-on-one movement sessions
Collaborations with studios
Website Structure
1: HOME
1.1.Hero Section: Large welcoming image
1.2 Two Main Pathways
- Bodywork: Kavenda® Structural Integration
- Movement & Education: Yoga, Pilates, trainings, workshops and retreats
- About Preview: Small introduction with portrait. + Button:
Read More
1.3 Current Events / What's Coming Up: Upcoming trainings, workshops and retreats. (This section should be easy to update)
1.4. Contact / Newsletter: Simple contact information
2: Kavenda® Structural Integration
What is Kavenda?
For whom is it?
What does a session look like?
FAQ
Prices
Booking
Future possibility:
Kaven Movement sessions
3: Movement
- Introductory text.
- Studio Classes (link to “my home base” - > local yoga studio)
- One-to-One Sessions: booking option (this is small; not a key aspect I want to promote)
- Workshops/ Retreats / Teacher Trainings => This section should be flexible and easy to update. Visitors should be able to click into specific offerings.
4. Events
Dynamic page for: Teacher trainings, Retreats, Workshops (see section in movement; here more elaborate)
Each event should contain: Image, Short description, Location, Date, Button for more information. (Linking to hosting studio/location)
5. Work With Me
For studios, organisations and teacher training schools.
Examples: Guest teaching, Workshops, Anatomy, Sequencing, Teacher development , Continuing education -> Clear call-to-action.
Call to action!!=> Book a Session
Prominent button in the navigation.
Footer:
- About Me: Longer biography (6th page)
Personal story and background.
- Testimonials (7th page): Separate page containing testimonials from:
Kavenda clients
Students
Teacher trainees
- Contact: 8th page
Visual Direction
Natural textures. Lots of white space.Editorial feeling.Professional photography.Simple navigation.
Less "wellness influencer.” More:Thoughtful, Contemporary, Timeless, Grounded, Human
Photography should show:
Teaching
Hands-on work
Natural movement
Real interaction
Simplicity
Avoid stereotypical yoga imagery and overly spiritual aesthetics.
Keywords
Warm. Curious. Human. Professional. Embodied. Intelligent. Accessible. Playful. Grounded. Exploratory. Real.
Inspiration / Core Message
Helping people feel more at home in their bodies through touch, movement and education.
The website should communicate that these are not separate services, but different expressions of the same intention:
Bodywork • Movement • Education.
Colours:
light orange/beige: e3d5c4
light orange/off white: f9f7f3
gray azure: 556b78
orange: d07b5a
grey orange: c09f80
dark grey: 3e3e3e
dark gray cyan 2f4f4f
gray green colour: a7c4a0
Fonts: Montserrat and Poppins + raleway
In added documents a try out idea of a website + logo. I will mainly use the logo with diffrent colours (image next to text).
My audience consists of people who want to feel more at home in their bodies and who appreciate a thoughtful, grounded and human approach to movement, touch and education. (30-65yo)
wellbeing
5+ page
- montserrat, poppins, raleway

```html
<!DOCTYPE html>
<html lang="en">
<head>
<meta charset="utf-8">
<title>Liesbet Oonwerk — Kavenda® Structural Integration</title>
<link rel="stylesheet" href="https://fonts.googleapis.com/css2?family=Poppins:wght@200;300;400;500;600&display=swap">
<style>
:root{
  --beige:#e3d5c4;
  --offwhite:#f9f7f3;
  --azure:#556b78;
  --orange:#d07b5a;
  --greyorange:#c09f80;
  --dark:#3e3e3e;
  --cyan:#2f4f4f;
  --green:#a7c4a0;
  --white:#ffffff;
}
*{margin:0;padding:0;box-sizing:border-box}
html,body{width:1200px;height:3220px;overflow:hidden}
body{font-family:'Poppins',sans-serif;color:var(--dark);background:var(--offwhite);position:relative}
.abs{position:absolute}
.eyebrow{font-size:9.5px;letter-spacing:3px;text-transform:uppercase;color:var(--orange);font-weight:500}
.btn{position:absolute;display:flex;align-items:center;justify-content:center;border-radius:30px;font-size:12.5px;font-weight:500;text-decoration:none;white-space:nowrap}
.btn-solid{background:var(--orange);color:var(--white)}
.btn-ghost{border:1.5px solid rgba(255,255,255,.85);color:var(--white)}

/* hero */
.hero{position:absolute;left:0;top:0;width:1200px;height:630px;overflow:hidden}
.hero-photo{position:absolute;inset:0;background:linear-gradient(180deg,#8d9a9c 0%,#9aa6a6 35%,#8a8a80 65%,#a39a8a 100%)}
.hero-curve{position:absolute;left:0;bottom:0}
.nav-logo{position:absolute;left:91px;top:22px;color:var(--white)}
.nav-logo .name{font-size:16px;font-weight:400;line-height:1.1}
.nav-logo .sub{font-size:6.5px;letter-spacing:.8px}
.nav{position:absolute;top:28px;right:243px;display:flex;gap:21px;font-size:11.5px;color:var(--white);white-space:nowrap}
.nav .active{color:var(--orange)}
.hero h1{position:absolute;left:91px;top:152px;font-weight:200;font-size:66px;line-height:73px;color:var(--white);letter-spacing:-.5px}
.hero p.lead{position:absolute;left:91px;top:390px;width:505px;font-size:15.5px;line-height:26px;color:var(--white)}
.hero-portrait{position:absolute;left:828px;top:195px;width:278px;height:278px;border-radius:50%;border:4px solid rgba(255,255,255,.55);background:radial-gradient(circle at 50% 40%,#efe6d8,#c8a57c 70%,#9b7a55)}

/* pathways */
.section-head{position:absolute;left:0;width:1200px;text-align:center}
.section-head h2{font-weight:200;font-size:46px;color:var(--dark);margin-top:14px}
.section-head p{font-size:14px;line-height:24px;color:var(--azure);margin-top:10px}
.path{position:absolute;width:426px;height:426px;border-radius:50%;box-shadow:0 18px 40px rgba(0,0,0,.15);color:var(--white);text-align:center;overflow:hidden}
.path .inner{position:absolute;left:0;right:0;top:138px}
.path h3{font-weight:400;font-size:25px}
.path p{font-size:12.5px;line-height:20px;margin-top:8px}
.path .btn{position:relative;margin:18px auto 0;display:inline-flex;padding:0 28px;height:46px}
.path-body{left:126px;top:895px;background:radial-gradient(circle at 50% 35%,#b9c4c4,#6e8584 55%,#2f3e33)}
.path-move{left:648px;top:895px;background:radial-gradient(circle at 50% 25%,#e9b085,#a4603b 50%,#3b2418)}

/* about */
.about{position:absolute;left:0;top:1410px;width:1200px;height:458px;background:var(--white)}
.about-portrait{position:absolute;left:93px;top:117px;width:228px;height:228px;border-radius:50%;border:3px solid var(--beige);background:radial-gradient(circle at 55% 40%,#8b6a4c,#4a3526 60%,#241a13);box-shadow:0 12px 28px rgba(0,0,0,.15)}
.about-text{position:absolute;left:376px;top:93px;width:740px}
.about-text h2{font-weight:200;font-size:45px;line-height:52px;margin-top:12px}
.about-text p{font-size:14px;line-height:24px;color:var(--dark)}
.about-text p.soft{color:var(--azure);margin-top:14px}
.about-text a{display:block;margin-top:16px;color:var(--orange);font-size:12.5px;text-decoration:none}

/* events */
.events{position:absolute;left:0;top:1868px;width:1200px;height:687px;background:var(--beige)}
.events h2{position:absolute;left:91px;top:112px;font-weight:200;font-size:46px}
.events .eyebrow{position:absolute;left:91px;top:98px}
.arrow{position:absolute;top:111px;width:38px;height:38px;border-radius:50%}
.event{position:absolute;top:200px;width:324px;height:324px;border-radius:50%;color:var(--white);text-align:center;box-shadow:0 12px 28px rgba(0,0,0,.1)}
.event .tag{display:inline-block;margin-top:130px;padding:4px 10px;border-radius:12px;background:rgba(255,255,255,.25);font-size:8px;letter-spacing:1px;font-weight:600;text-transform:uppercase}
.event h4{font-weight:400;font-size:13px;margin-top:4px}
.event p{font-size:10px}
.ev1{left:91px;background:radial-gradient(circle at 50% 25%,#e5ac82,#9c5b38 50%,#3a2317)}
.ev2{left:438px;background:radial-gradient(circle at 50% 30%,#c89a62,#6b4d2e 55%,#2e2418)}
.ev3{left:784px;background:radial-gradient(circle at 50% 30%,#c3cbd1,#9aa3a6 55%,#8b7e6a)}

/* newsletter */
.news{position:absolute;left:91px;top:2645px;width:1018px;height:140px;border-radius:70px;background:var(--white);box-shadow:0 10px 30px rgba(0,0,0,.04)}
.news h3{position:absolute;left:50px;top:42px;font-weight:300;font-size:25px}
.news p{position:absolute;left:50px;top:82px;font-size:12px;color:var(--azure)}
.news .field{position:absolute;left:578px;top:48px;width:263px;height:45px;border:1px solid var(--beige);border-radius:25px;background:var(--offwhite);font-size:12px;color:#9a9a9a;padding:13px 20px}
.news .btn{left:850px;top:48px;width:118px;height:45px}

/* footer */
.footer{position:absolute;left:0;top:2870px;width:1200px;height:350px}
.footer .bg{position:absolute;left:0;top:0}
.fcol{position:absolute;top:80px;color:var(--white)}
.fcol h5{font-size:12.5px;font-weight:500}
.fcol ul{list-style:none;margin-top:14px}
.fcol li{font-size:11.5px;color:#b8b8b8;line-height:26px}
.fcol p{font-size:11.5px;color:#b8b8b8;line-height:20px;margin-top:12px}
.copy{position:absolute;left:0;top:318px;width:1200px;text-align:center;font-size:9px;color:#8d8d8d}
</style>
</head>
<body>

<header class="hero">
  <div class="hero-photo" role="img" aria-label="Balanced stack of smooth pebbles on a pebble beach at soft grey dusk"></div>
  <svg class="hero-curve" width="1200" height="130" viewBox="0 0 1200 130"><path d="M0 10 Q600 230 1200 10 L1200 130 L0 130Z" fill="#f9f7f3"/></svg>

  <div class="nav-logo"><div class="name">Liesbet Oonwerk</div><div class="sub">Kavenda® Structural Integration</div></div>
  <nav class="nav"><span class="active">Home</span><span>Kavenda</span><span>Movement</span><span>Events</span><span>Work With Me</span><span>About</span><span>Testimonials</span><span>Contact</span></nav>
  <a class="btn btn-solid" style="left:982px;top:17px;width:127px;height:38px;font-size:11.5px;font-weight:400">Book a Session</a>

  <div class="eyebrow abs" style="left:91px;top:127px">Kavenda® · Movement · Education</div>
  <h1>Feel more at<br>home<br>in your body.</h1>
  <p class="lead">Touch · Movement · Education — helping you reconnect with your body through Kavenda® Structural Integration, yoga, and embodied learning.</p>
  <a class="btn btn-ghost" style="left:91px;top:492px;width:157px;height:46px">Discover Kavenda</a>
  <a class="btn btn-solid" style="left:258px;top:492px;width:147px;height:46px">Book a Session</a>

  <div class="hero-portrait" role="img" aria-label="Group movement class practising partner exercises in a bright studio"></div>
</header>

<section>
  <div class="section-head" style="top:720px">
    <div class="eyebrow">Explore my work</div>
    <h2>Bodywork · Movement · Education</h2>
    <p>Three expressions of the same intention: helping you feel<br>more at home in your body.</p>
  </div>
  <div class="path path-body" role="img" aria-label="Person balancing in tree pose on a misty mountainside">
    <div class="inner"><h3>Bodywork: Kavenda®</h3><p>Hands-on support to bring your body<br>into better alignment, ease and vitality.</p><a class="btn btn-ghost">Learn More</a></div>
  </div>
  <div class="path path-move" role="img" aria-label="Person seated with open arms at sunset on a wooden deck">
    <div class="inner"><h3>Movement &amp; Education</h3><p>Yoga, Pilates, workshops and teacher<br>trainings grounded in curiosity.</p><a class="btn btn-ghost">Explore</a></div>
  </div>
</section>

<section class="about">
  <div class="about-portrait" role="img" aria-label="Portrait of the practitioner in warm side light"></div>
  <div class="about-text">
    <div class="eyebrow">About me</div>
    <h2>Rooted in curiosity,<br>guided by the body.</h2>
    <p>My work lives at the intersection of touch, movement and education. As a certified Kavenda® practitioner, yoga teacher and movement educator, I help people feel more at home in themselves.</p>
    <p class="soft">I believe the body is not something to fix, but something to listen to. My approach is grounded in science, lived experience, and a deep respect for each person’s unique path.</p>
    <a>Read my full story</a>
  </div>
</section>

<section class="events">
  <div class="eyebrow">What’s coming up</div>
  <h2>Upcoming Events</h2>
  <svg class="arrow" style="left:1017px" viewBox="0 0 38 38"><circle cx="19" cy="19" r="19" fill="#ede4d8"/><path d="M26 19H12M16 15l-4 4 4 4" stroke="#b8a996" stroke-width="1.4" fill="none"/></svg>
  <svg class="arrow" style="left:1069px" viewBox="0 0 38 38"><circle cx="19" cy="19" r="19" fill="#fff"/><path d="M12 19h14M22 15l4 4-4 4" stroke="#3e3e3e" stroke-width="1.4" fill="none"/></svg>
  <div class="event ev1" role="img" aria-label="Person with open arms at sunset"><span class="tag">Workshop</span><h4>Embodied Anatomy</h4><p>Jun 24–28 · Antwerp</p></div>
  <div class="event ev2" role="img" aria-label="Yoga class in a warm wooden studio"><span class="tag">Training</span><h4>YTT — Module 1</h4><p>Sep 12–14 · Brussels</p></div>
  <div class="event ev3" role="img" aria-label="Group in tree pose on a beach"><span class="tag">Retreat</span><h4>Autumn Retreat</h4><p>Oct 5–10 · Portugal</p></div>
  <a class="btn" style="left:527px;top:554px;width:146px;height:45px;background:var(--dark);color:var(--white)">View all events</a>
</section>

<section class="news">
  <h3>Stay connected</h3>
  <p>Occasional updates on workshops, retreats and new offerings.</p>
  <div class="field">Your email</div>
  <a class="btn btn-solid">Subscribe</a>
</section>

<footer class="footer">
  <svg class="bg" width="1200" height="350" viewBox="0 0 1200 350"><path d="M0 60 Q600 -40 1200 60 L1200 350 L0 350Z" fill="#3e3e3e"/></svg>
  <div class="fcol" style="left:91px"><h5>Liesbet Oonwerk</h5><p>Kavenda® Structural Integration · Movement · Education</p><p>Helping people feel more at home in their bodies through<br>touch, movement and education.</p></div>
  <div class="fcol" style="left:489px"><h5>Explore</h5><ul><li>Kavenda</li><li>Movement</li><li>Events</li><li>Work With Me</li></ul></div>
  <div class="fcol" style="left:710px"><h5>About</h5><ul><li>About Me</li><li>Testimonials</li><li>Contact</li></ul></div>
  <div class="fcol" style="left:930px"><h5>Connect</h5><ul><li>Lenswall</li><li>Circlebook</li><li>Workthread</li><li>Email</li></ul></div>
  <div class="copy">© 2026 Liesbet Oonwerk. All rights reserved. Kavenda® is a registered trademark of the Orenvale Bodywork Institute®.</div>
</footer>

</body>
</html>
```